New Business Card

We need to refresh our business cards. We designed these ourselves and we have no graphic design experience. We would like to find a new business card design that is professional and unique. We are an auto finance company. Feel free to play with the logo, but we would like to keep the eye very present on the card. Our corporate colors are green, grey, and white.
Green - RGB - 168,215,27; HEX - #AADD22
Grey - RGB - 196,196,196; HEX - #C4C4C4
Updates
Need to upload the vector file to finalize the project. The last logo was for a jpeg that didn't stretch well.
Industry/Entity Type
Financial Service
Contact Information for Business Card
Honestly don't know...I need your help!

```html
<!DOCTYPE html>
<html lang="en">
<head>
<meta charset="utf-8">
<title>Brightlane Capital – Business Card</title>
<link href="https://fonts.googleapis.com/css2?family=Open+Sans:wght@600&family=Tinos:wght@400&display=swap" rel="stylesheet">
<style>
  :root {
    --brand-green: #AADD22;
    --brand-grey: #C4C4C4;
    --panel-grey: #BDBDBD;
    --card-white: #FAFAF8;
    --stage: #E6E4E0;
    --ink-white: #FFFFFF;
  }
  * { box-sizing: border-box; margin: 0; padding: 0; }
  html, body {
    width: 1200px; height: 960px; overflow: hidden;
    background: var(--stage);
  }
  .sheet {
    width: 1200px; height: 960px;
    display: flex; flex-direction: column; align-items: center; justify-content: center;
    gap: 60px;
  }
  .card {
    width: 630px; height: 360px;
    background: var(--card-white);
    box-shadow: 0 2px 6px rgba(0,0,0,0.12);
    position: relative; overflow: hidden;
  }

  /* Back side */
  .card--back { display: flex; }
  .contact-panel {
    width: 46%; height: 100%;
    background: var(--panel-grey);
    color: var(--ink-white);
    display: flex; flex-direction: column; align-items: center;
    padding-top: 54px;
  }
  .contact-panel .wordmark {
    font-family: "Open Sans", sans-serif; font-weight: 600;
    text-align: center; line-height: 1;
  }
  .contact-panel .wordmark__name { display: block; font-size: 44px; letter-spacing: -0.5px; }
  .contact-panel .wordmark__sub { display: block; font-size: 13px; letter-spacing: 9px; margin-top: 6px; padding-left: 9px; }
  .person {
    font-family: "Tinos", serif; text-align: center; margin-top: 14px;
  }
  .person__name {
    font-size: 28px; border-bottom: 1.5px solid var(--ink-white);
    padding: 0 6px 1px; display: inline-block;
  }
  .person__title { font-size: 14px; margin-top: 2px; }
  .contact-list {
    list-style: none; font-family: "Tinos", serif; font-size: 12.5px;
    margin-top: 8px; line-height: 1.55;
  }
  .contact-list li { display: flex; align-items: center; gap: 6px; }
  .contact-list svg { width: 10px; height: 13px; }
  .mark-side {
    flex: 1; display: flex; align-items: center; justify-content: center;
  }
  .brand-dot {
    width: 150px; height: 150px; border-radius: 50%;
    background: var(--brand-green);
  }

  /* Front side */
  .card--front {
    display: flex; flex-direction: column; align-items: center; justify-content: center;
    gap: 22px;
  }
  .card--front .brand-dot { width: 120px; height: 120px; }
  .card--front .wordmark {
    font-family: "Open Sans", sans-serif; font-weight: 600;
    color: var(--brand-green); text-align: center; line-height: 1;
  }
  .card--front .wordmark__name { display: block; font-size: 54px; letter-spacing: -0.5px; }
  .card--front .wordmark__sub { display: block; font-size: 19px; letter-spacing: 12px; margin-top: 8px; padding-left: 12px; }
</style>
</head>
<body>
<main class="sheet">
  <section class="card card--back" aria-label="Card back">
    <div class="contact-panel">
      <p class="wordmark"><span class="wordmark__name">Brightlane</span><span class="wordmark__sub">CAPITAL</span></p>
      <div class="person">
        <p class="person__name">Dana Whitfield</p>
        <p class="person__title">President</p>
      </div>
      <ul class="contact-list">
        <li>
          <svg viewBox="0 0 10 13" aria-hidden="true"><rect x="1" y="0.5" width="8" height="12" rx="1.5" fill="none" stroke="#fff" stroke-width="1"/><circle cx="5" cy="10.5" r="0.8" fill="#fff"/></svg>
          000-000-0000
        </li>
        <li>
          <svg viewBox="0 0 10 13" aria-hidden="true"><path d="M2 1.5 L4 1 L5 4 L3.6 5 Q4.5 7.8 6.5 9 L7.5 8 L9.5 9.5 L9 11.5 Q3 11 1.5 3 Z" fill="#fff"/></svg>
          555-010-4420
        </li>
        <li>
          <svg viewBox="0 0 10 13" aria-hidden="true"><rect x="0.5" y="3" width="9" height="7" fill="none" stroke="#fff" stroke-width="1"/><path d="M0.5 3 L5 7 L9.5 3" fill="none" stroke="#fff" stroke-width="1"/></svg>
          info@brightlane.com
        </li>
      </ul>
    </div>
    <div class="mark-side"><div class="brand-dot" aria-hidden="true"></div></div>
  </section>

  <section class="card card--front" aria-label="Card front">
    <div class="brand-dot" aria-hidden="true"></div>
    <p class="wordmark"><span class="wordmark__name">Brightlane</span><span class="wordmark__sub">CAPITAL</span></p>
  </section>
</main>
</body>
</html>
```